Design a Coloring Book Cover

Please help us create a 8.5 x 11 inch coloring book cover. As you can tell from the title, it is a Christian adult coloring book.

Title: Sparrow Window Pages
Subtitle: The Inspirational Christian Adult Coloring Book (Religious Themes and Inspiring Phrases)

You can look at some covers here for some ideas...http://www.shelvoria-market.example/s/ref=nb_sb_ss_i_1_11?url=search-alias%3Dstripbooks&field-keywords=christian+coloring+books&sprefix=christian+c%2Cstripbooks%2C252

```html
<!DOCTYPE html>
<html lang="en">
<head>
<meta charset="UTF-8">
<title>Sparrow Window Pages – Coloring Book Cover</title>
<link rel="stylesheet" href="https://fonts.googleapis.com/css2?family=Yellowtail&family=Montserrat:wght@500;600;700&display=swap">
<style>
  :root {
    --paper: #f7f7f7;
    --ink: #111111;
    --rose: #e06aa8;
    --rose-deep: #c8348a;
    --rose-soft: #f3b9c6;
    --petal-cream: #f6ecd9;
    --leaf: #8c8f78;
    --butterfly-mauve: #b58aa2;
    --white: #ffffff;
  }
  html, body {
    margin: 0;
    padding: 0;
    width: 927px;
    height: 1200px;
    overflow: hidden;
    background: var(--paper);
  }
  .cover {
    position: relative;
    width: 927px;
    height: 1200px;
    background: var(--paper);
    overflow: hidden;
    font-family: "Montserrat", sans-serif;
  }
  .butterfly-band {
    position: absolute;
    left: 0;
    top: 0;
    width: 927px;
    height: 118px;
    background: linear-gradient(90deg, #f4d7df 0%, #eccbd8 25%, #f6d9dc 50%, #e9cad6 75%, #f4d7df 100%);
  }
  .wreath {
    position: absolute;
    left: 0;
    top: 0;
    width: 927px;
    height: 1200px;
  }
  .title {
    position: absolute;
    margin: 0;
    font-family: "Yellowtail", cursive;
    font-weight: 400;
    line-height: 1;
    color: var(--ink);
  }
  .title-line-one { left: 248px; top: 395px; font-size: 120px; }
  .title-line-two { left: 300px; top: 535px; font-size: 116px; }
  .title-line-three { left: 340px; top: 690px; font-size: 140px; color: var(--rose); }
  .format-banner {
    position: absolute;
    left: 160px;
    top: 900px;
    width: 600px;
    height: 110px;
  }
  .format-label {
    position: absolute;
    left: 160px;
    top: 928px;
    width: 600px;
    text-align: center;
    font-family: "Montserrat", sans-serif;
    font-weight: 600;
    font-size: 40px;
    letter-spacing: 1px;
    color: var(--white);
    transform: rotate(-1.5deg);
  }
  .subtitle {
    position: absolute;
    left: 0;
    top: 1078px;
    width: 927px;
    margin: 0;
    text-align: center;
    font-family: "Montserrat", sans-serif;
    font-weight: 600;
    font-size: 21px;
    line-height: 34px;
    letter-spacing: 0.6px;
    color: var(--ink);
  }
</style>
</head>
<body>
<main class="cover">
  <div class="butterfly-band" role="img" aria-label="Repeating band of pink, mauve and grey butterflies"></div>

  <svg class="wreath" viewBox="0 0 927 1200" role="img" aria-label="Circular wreath of pink peonies, cream blossoms and green leaves">
    <defs>
      <radialGradient id="wreath-tone" cx="50%" cy="50%" r="50%">
        <stop offset="62%" stop-color="#f6ecd9"/>
        <stop offset="78%" stop-color="#f0c3cc"/>
        <stop offset="90%" stop-color="#d9b0b3"/>
        <stop offset="100%" stop-color="#c4c8b4"/>
      </radialGradient>
    </defs>
    <path fill="url(#wreath-tone)" fill-rule="evenodd" opacity="0.85"
      d="M470 196 a420 420 0 1 0 0.1 0 Z M470 336 a278 278 0 1 1 -0.1 0 Z"/>
    <circle cx="470" cy="616" r="278" fill="var(--paper)"/>
  </svg>

  <h1 class="title-block">
    <span class="title title-line-one">Sparrow</span>
    <span class="title title-line-two">Window</span>
    <span class="title title-line-three">Pages</span>
  </h1>

  <svg class="format-banner" viewBox="0 0 600 110" aria-hidden="true">
    <path d="M6 40 L590 14 L596 82 L12 102 Z" fill="var(--rose-deep)"/>
    <path d="M0 52 L26 36 L20 98 L2 90 Z" fill="var(--rose)" opacity="0.7"/>
  </svg>
  <div class="format-label">COLORING BOOK</div>

  <p class="subtitle">The Inspirational Christian Adult Coloring Book<br>Religious Themes and Inspiring Phrases</p>
</main>
</body>
</html>
```